Corporate Design für Rechtsanwaltskanzlei
Zielgruppe
Rechtsanwaltskanzlei
spezialisiert im Bereich Arbeitsrecht und Handels- und Gesellschaftsrecht
Zielgruppe Firmen, Geschäftsführer, Privatpersonen
Aufgabenstellung
Ich bin Fachanwältin für Handels- und Gesellschaftsrecht und Fachanwältin für Arbeitsrecht. Diese Titel müssen auf dem Briefpapier und der Visitenkarte erscheinen, nicht aber im Logo
Ich füge mein aktuelles Briefpapier zur Orientierung für den Inhalt bei.
Das Design sollte sympathisch sein, nicht zu konservativ und weiblich und Kompetenz ausstrahlen.

```html
<!DOCTYPE html>
<html lang="de">
<head>
<meta charset="utf-8">
<title>Kanzlei Rieg – Corporate Design</title>
<link href="https://fonts.googleapis.com/css2?family=Montserrat:wght@400;500&family=Open+Sans:wght@400;600&display=swap" rel="stylesheet">
<style>
:root{
  --red:#981b2e;
  --ink:#1f1e1d;
  --grey:#3b3b3b;
  --board:#e1e2e1;
  --paper:#f7f8fa;
  --white:#ffffff;
  --faint:#e4e4e6;
}
*{margin:0;padding:0;box-sizing:border-box}
html,body{width:1200px;height:1200px;overflow:hidden;background:var(--white)}
body{position:relative;font-family:"Open Sans",sans-serif;color:var(--grey)}
.board{position:absolute;left:73px;top:0;width:1053px;height:1200px;background:var(--board)}
.abs{position:absolute}

/* logo lockup */
.lockup{position:absolute;display:flex;flex-direction:column;align-items:flex-start}
.lockup .name{display:flex;align-items:center;gap:.35em;font-family:"Montserrat",sans-serif;font-weight:500;white-space:nowrap;letter-spacing:.02em}
.lockup .mark{width:.7em;height:.7em;background:var(--red)}
.lockup .sub{font-family:"Montserrat",sans-serif;font-weight:400;white-space:nowrap;margin-top:.35em;letter-spacing:.01em}
.on-white .name,.on-white .sub{color:var(--grey)}
.on-dark .name,.on-dark .sub{color:var(--white)}
.mark-white .mark{background:var(--white)}
.mark-grey .mark{background:var(--grey)}

/* presentation panel */
.panel-white{left:232px;top:66px;width:247px;height:206px;background:var(--white)}
.panel-red{left:479px;top:66px;width:486px;height:103px;background:var(--red)}
.panel-dark{left:479px;top:169px;width:486px;height:103px;background:var(--ink)}
.panel-lockup .name{font-size:15px}
.panel-lockup .sub{font-size:9.5px}

/* business cards */
.label{font-size:8px;color:var(--ink)}
.card{position:absolute;top:311px;width:179px;height:116px}
.card-dark{background:var(--ink)}
.card-dark .lockup{left:34px;top:52px}
.card-dark .name{font-size:9.5px}
.card-dark .sub{font-size:5.2px}
.card-claim{position:absolute;left:0;right:0;bottom:10px;text-align:center;font-size:5px;letter-spacing:.12em;color:var(--white);font-weight:600}
.card-claim .sep{color:var(--white);margin:0 3px}
.card-claim .dot{color:var(--red);margin:0 3px}
.card-light{background:var(--white);left:858px}
.card-light .who{position:absolute;left:12px;top:14px;font-family:"Montserrat",sans-serif;font-size:10px;color:var(--grey);display:flex;align-items:center;gap:5px}
.card-light .who .mark{width:8px;height:8px;background:var(--red)}
.card-light .titles{position:absolute;left:67px;top:28px;font-size:4.6px;line-height:1.4}
.card-light .contact{position:absolute;top:94px;font-size:4.6px;line-height:1.5}

/* letterhead */
.letter{left:237px;top:489px;width:331px;height:467px;background:var(--paper)}
.letter .lockup{left:27px;top:20px}
.letter .lockup .name{font-size:10px}
.letter .lockup .sub{font-size:5.4px}
.letter .divider{position:absolute;left:149px;top:32px;width:1px;height:25px;background:var(--grey)}
.letter .titles{position:absolute;left:158px;top:37px;font-size:6.6px;line-height:1.35}
.letter .small{font-size:4px}
.letter .sender{position:absolute;left:34px;top:70px}
.letter .recipient{position:absolute;left:34px;top:81px;font-size:5px;line-height:1.35}
.letter .greeting{position:absolute;left:34px;top:148px;font-size:6px;letter-spacing:.05em}
.letter .body{position:absolute;left:34px;width:262px;font-size:5.6px;line-height:1.3}
.letter .fold{position:absolute;left:0;width:9px;height:1px;background:#9a9a9a}
.letter .signature{position:absolute;left:205px;top:383px;width:72px;height:36px;background:linear-gradient(90deg,rgba(59,59,59,.06),rgba(59,59,59,.14),rgba(59,59,59,.06));border-radius:18px}
.letter .foot{position:absolute;top:433px;font-size:3.6px;line-height:1.35}
.letter .foot-rule{position:absolute;top:432px;width:1.2px;height:27px;background:var(--red)}
.letter .band{position:absolute;left:0;bottom:0;width:100%;height:7px;background:var(--red)}

/* folder */
.folder{left:644px;top:484px;width:330px;height:467px;background:var(--red)}
.folder .spine{position:absolute;top:0;height:100%;width:1px;background:rgba(0,0,0,.25)}
.folder .lockup{left:90px;top:222px}
.folder .lockup .name{font-size:18px}
.folder .lockup .sub{font-size:11px}
.folder .url{position:absolute;left:0;right:0;top:445px;text-align:center;font-size:9px;letter-spacing:.2em;color:var(--white)}

/* envelopes */
.envelope{left:229px;top:992px;width:346px;height:175px;background:var(--paper)}
.envelope .lockup{left:34px;top:22px}
.envelope .lockup .name{font-size:9.5px}
.envelope .lockup .sub{font-size:5.2px}
.envelope .window{position:absolute;left:32px;top:76px;width:158px;height:69px;background:#d0d0d1;border-radius:4px}
.envelope .deco{position:absolute;left:214px;top:66px;width:86px;height:86px;border-radius:50%;background:var(--faint)}
.envelope .band{position:absolute;left:0;bottom:0;width:100%;height:7px;background:var(--red)}
.envelope-flap{left:638px;top:994px;width:346px;height:173px;background:var(--white)}
.envelope-flap svg{position:absolute;left:0;top:0}
.envelope-flap .flap-name{position:absolute;left:0;right:0;top:28px;text-align:center;font-family:"Montserrat",sans-serif;font-weight:500;font-size:14px;letter-spacing:.15em;color:var(--white)}
.envelope-flap .url{position:absolute;left:0;right:0;top:162px;text-align:center;font-size:6.5px;letter-spacing:.2em;color:var(--grey)}
</style>
</head>
<body>
<div class="board"></div>

<!-- logo variants -->
<section class="abs panel-white"></section>
<section class="abs panel-red"></section>
<section class="abs panel-dark"></section>

<div class="lockup panel-lockup on-white" style="left:262px;top:112px">
  <div class="name"><span class="mark"></span>Dr. CARLA RIEG</div>
  <div class="sub">KANZLEI FÜR WIRTSCHAFTSRECHT</div>
</div>
<div class="lockup panel-lockup on-white mark-grey" style="left:262px;top:213px">
  <div class="name"><span class="mark"></span>Dr. CARLA RIEG</div>
  <div class="sub">KANZLEI FÜR WIRTSCHAFTSRECHT</div>
</div>
<div class="lockup panel-lockup on-dark mark-white" style="left:630px;top:112px">
  <div class="name"><span class="mark"></span>Dr. CARLA RIEG</div>
  <div class="sub">KANZLEI FÜR WIRTSCHAFTSRECHT</div>
</div>
<div class="lockup panel-lockup on-dark" style="left:513px;top:213px">
  <div class="name"><span class="mark"></span>Dr. CARLA RIEG</div>
  <div class="sub">KANZLEI FÜR WIRTSCHAFTSRECHT</div>
</div>
<div class="lockup panel-lockup on-dark mark-white" style="left:733px;top:213px">
  <div class="name"><span class="mark"></span>Dr. CARLA RIEG</div>
  <div class="sub">KANZLEI FÜR WIRTSCHAFTSRECHT</div>
</div>

<!-- business cards -->
<span class="abs label" style="left:116px;top:301px">A</span>
<span class="abs label" style="left:334px;top:301px">B</span>
<span class="abs label" style="left:573px;top:301px">C</span>

<article class="card card-dark" style="left:134px">
  <div class="lockup on-dark"><div class="name"><span class="mark"></span>Dr. CARLA RIEG</div><div class="sub">KANZLEI FÜR WIRTSCHAFTSRECHT</div></div>
  <p class="card-claim">ENGAGIERT<span class="sep">|</span>KOMPETENT<span class="sep">|</span>PERSÖNLICH</p>
</article>
<article class="card card-dark" style="left:352px">
  <div class="lockup on-dark"><div class="name"><span class="mark"></span>Dr. CARLA RIEG</div><div class="sub">KANZLEI FÜR WIRTSCHAFTSRECHT</div></div>
  <p class="card-claim">ENGAGIERT<span class="dot">•</span>KOMPETENT<span class="dot">•</span>PERSÖNLICH</p>
</article>
<article class="card card-dark" style="left:591px">
  <div class="lockup on-dark"><div class="name"><span class="mark"></span>Dr. CARLA RIEG</div><div class="sub">KANZLEI FÜR WIRTSCHAFTSRECHT</div></div>
  <p class="card-claim">ENGAGIERT<span class="dot">▪</span>KOMPETENT<span class="dot">▪</span>PERSÖNLICH</p>
</article>
<article class="card card-light">
  <div class="who"><span class="mark"></span>Dr. Carla Rieg</div>
  <p class="titles">Fachanwältin für Handels- und Gesellschaftsrecht<br>Fachanwältin für Arbeitsrecht</p>
  <p class="contact" style="left:13px">Lindenweg 8<br>42103 Musterstadt</p>
  <p class="contact" style="left:65px">T. 0202 / 4418203<br>F. 0202/4418209</p>
  <p class="contact" style="left:117px">rieg@kanzleirieg.de<br>www.kanzleirieg.de</p>
</article>

<!-- letterhead -->
<article class="abs letter">
  <div class="lockup on-white"><div class="name"><span class="mark"></span>Dr. CARLA RIEG</div><div class="sub">KANZLEI FÜR WIRTSCHAFTSRECHT</div></div>
  <span class="divider"></span>
  <p class="titles">Fachanwältin für Handels- und Gesellschaftsrecht<br>Fachanwältin für Arbeitsrecht</p>
  <p class="sender small">Dr. CARLA RIEG &nbsp;| Lindenweg 8 | 42103 Musterstadt</p>
  <p class="recipient">Recipient Name<br>Organization Name<br>Street Address<br>City - Zip Code</p>
  <span class="fold" style="top:154px"></span>
  <span class="fold" style="top:232px"></span>
  <span class="fold" style="top:310px"></span>
  <p class="greeting">Dear Name Here,</p>
  <p class="body" style="top:182px">Lorem ipsum dolor sit amet, consectetur adipiscing elit. Donec cursus eget dq-mauris sit amet elementum. Sed sed malesuada urna. Aliquam commodo velithquis rutrum finibus. Vivamus non consequat urna. Fusce dapibus risus quis mhpellentesque, id pretium lorem ornare. Aenean ac sapien non sem ultricies fegt tempor. Proin feugiat rutrum purus vitae facilisis. Mauris finibus lacus nec feaq metus ornare, sed consequat felis congue. Integer cursus suscipit pretium. ute Morbi tincidunt vel ipsum nec mollis. Interdum et malesuada fames ac ante litru ipsum primis in faucibus.</p>
  <p class="body" style="top:248px">Cras aliquam libero id sem iaculis eleifend vitae non mauris. Nam volutpat elittquis interdum pulvinar. Vestibulum ac malesuada nisi. Curabitur malesuada ulyr tellus ante, quis iaculis ante scelerisque ut. Sed semper egestas porttitor. Nunc purus risus, rutrum in dapibus sed, dapibus et justo. Nulla in magna cumtempor, mattis lectus quis, ultricies sapien. Lorem ipsum dolor sit amet, consectetur adipiscing elit. Proin eget venenatis mi. Integer at justo congue, urluctus ipsum quis, gravida dui. Aenean in tellus sapien. Donec non sapien quismassa elementum ornare ut eu tortor. Donec erat urna, pulvinar id porttitor an.</p>
  <p class="body" style="top:307px">Dgnissim in urna. Nunc dolor risus, ultricies ac tortor a, aliquet varius nisi. Class aptent taciti sociosqu ad litora torquent per conubia nostra, per inceptos himenaeos. Aenean fringilla porta vestibulum. Phasellus ultrices ligula maur, re- vel sagittis nulla vestibulum at. Nulla facilisis dapibus lectus, ut tristique nunc repulvinar sed. In ornare feugiat lobortis. Sed in blandit nisi, vitae pulvinar nisire. Nulla a nulla nisl. Nullam purus tellus, sollicitudin vitae venenatis consectetur. rutrum non quam. Vestibulum in odio viverra, iaculis orci sit amet, ultrices cum massa. Aenean semper, purus vel porta condimentum, ex justo posuere diamo, ec auctor massa turpis sed</p>
  <div class="signature" role="img" aria-label="Handschriftliche Unterschrift"></div>
  <p class="foot" style="left:37px">Dr. CARLA RIEG<br>Lindenweg 8<br>42103 Musterstadt<br>Umsatzsteuer ID &nbsp;&nbsp;DE000000000</p>
  <span class="foot-rule" style="left:114px"></span>
  <p class="foot" style="left:130px">Tel. 0202 / 4418203<br>Fax. 0202/4418209<br>rieg@kanzleirieg.de<br>www.kanzleirieg.de</p>
  <span class="foot-rule" style="left:183px"></span>
  <p class="foot" style="left:200px">Bankverbindung<br>IBAN<br>BIC</p>
  <p class="foot" style="left:239px">XXXXXXXXXX<br>DE00 0000 0000 0000 0000 00<br>XXXXXXX</p>
  <span class="band"></span>
</article>

<!-- folder -->
<article class="abs folder">
  <span class="spine" style="left:8px"></span>
  <span class="spine" style="left:14px"></span>
  <span class="spine" style="left:28px"></span>
  <div class="lockup on-dark mark-white"><div class="name"><span class="mark"></span>Dr. CARLA RIEG</div><div class="sub">KANZLEI FÜR WIRTSCHAFTSRECHT</div></div>
  <p class="url">www.kanzleirieg.de</p>
</article>

<!-- envelope front -->
<article class="abs envelope">
  <div class="lockup on-white"><div class="name"><span class="mark"></span>Dr. CARLA RIEG</div><div class="sub">KANZLEI FÜR WIRTSCHAFTSRECHT</div></div>
  <span class="window"></span>
  <span class="deco"></span>
  <span class="band"></span>
</article>

<!-- envelope back -->
<article class="abs envelope-flap">
  <svg width="346" height="62" viewBox="0 0 346 62" aria-hidden="true">
    <path d="M1 0 H345 L336 52 Q334 60 326 60 H20 Q12 60 10 52 Z" fill="var(--red)"/>
  </svg>
  <p class="flap-name">RIEG</p>
  <p class="url">www.kanzleirieg.de</p>
</article>
</body>
</html>
```